Restaurant business revamping our look and need a new modern menu

We need a new menu that is appealing, similar to the look of our new logo while also keeping our "cozy, clean, Midland staple" feel and gets peoples eyes on the high price items and top sellers. We are a deli that's been around since 1984, with lots of Burgers, Curly Fries, Reuben, Salads, etc.
Once we like that menu, we will need our pizza specials menu updated to look similar.

Please refer to our website for menu word format www.tolbertsofcrestvale.com

Target Market(s)

Every day Midlanders

Industry/Entity Type

Restaurant

Requirements
Must have
• Current menu is a trifold - not a must have but nice layout

```html
<!DOCTYPE html>
<html lang="en">
<head>
<meta charset="utf-8">
<title>Tolbert's Deli Menu</title>
<link href="https://fonts.googleapis.com/css2?family=Libre+Baskerville:wght@400;700&display=swap" rel="stylesheet">
<style>
:root{
  --backdrop:#4a3526;
  --paper:#eee8dc;
  --ink:#17130f;
  --ink-soft:#2b251f;
}
*{box-sizing:border-box;margin:0;padding:0}
html,body{width:1200px;height:1200px;overflow:hidden}
body{background:var(--backdrop);font-family:"Libre Baskerville",Georgia,serif;color:var(--ink)}
.menu{position:absolute;left:20px;top:20px;width:1160px;height:1160px;background:var(--paper)}
.menu-frame{position:absolute;inset:12px 14px;border:5px double var(--ink)}
.panel{position:absolute;border:6px double var(--ink);background:var(--paper)}
.panel-cap{position:absolute;border:6px double var(--ink);border-bottom:none;background:var(--paper);border-radius:50% 50% 0 0/100% 100% 0 0;z-index:2}
.panel-body{position:absolute;z-index:3;display:flex;flex-direction:column;justify-content:space-between}
.panel-title{position:absolute;z-index:4;text-align:center;font-weight:700;line-height:1.05}
.item-name{font-weight:700;font-size:15px;line-height:1.2}
.item-desc{font-size:12.5px;line-height:1.3;color:var(--ink-soft)}
.row{display:flex;justify-content:space-between;align-items:flex-end;gap:8px}
.price{font-weight:700;font-size:13px;white-space:nowrap}
.sub{font-size:12.5px;line-height:1.3}
.burgers .item-name{font-size:14px}
.burgers .item-desc{font-size:11px;line-height:1.2}
.burgers .price{font-size:12.5px}
.sandwiches .item-name{font-size:14.5px}
.sandwiches .item-desc{font-size:11.5px;line-height:1.22}
.sandwiches .price{font-size:12.5px}
.brand{position:absolute;left:432px;top:34px;width:293px;height:206px;display:flex;align-items:center;justify-content:center}
.brand-name{font-size:46px;font-weight:700;line-height:1}
.drinks-list{font-size:11px;font-weight:700;line-height:1.6}
.note{font-size:10.6px;line-height:1.26;text-align:justify}
.contact{text-align:center;font-weight:700;font-size:17.5px;line-height:1.55}
</style>
</head>
<body>
<main class="menu">
  <div class="menu-frame"></div>

  <!-- Salads -->
  <div class="panel" style="left:40px;top:104px;width:374px;height:866px"></div>
  <div class="panel-cap" style="left:82px;top:52px;width:290px;height:66px"></div>
  <h2 class="panel-title" style="left:40px;width:374px;top:78px;font-size:36px">Salads</h2>
  <section class="panel-body salads" style="left:60px;top:140px;width:336px;height:816px">
    <div><div class="item-name">Chicken Salad Plate</div>
      <div class="row item-desc"><span>Chicken salad served on tomato wedge or avocado half, with Swiss and cheddar cheese and a side order of your choice.</span><span class="price">9.95</span></div></div>
    <div><div class="item-name">Tuna or Krab Salad Plate</div>
      <div class="row item-desc"><span>Tuna or Krab salad served on tomato wedge or avocado half, with Swiss and cheddar cheese and a side order of your choice.</span><span class="price">10.75</span></div></div>
    <div><div class="item-name">Fit “Chick”en</div>
      <div class="row item-desc"><span>Grilled or Blackened Chicken served on a bed of spinach with half an avocado and Tolbert’s steam grilled veggies with your choice of salad dressing...</span><span class="price">13.09</span></div>
      <div class="row sub"><span>With grilled or blackened salmon, shrimp or Tuna...</span><span class="price">15.05</span></div></div>
    <div><div class="row"><span class="item-name">Caesar Salad</span><span class="price">6.09</span></div>
      <div class="row sub"><span>Add grilled or blackened chicken breast...</span><span class="price">8.09</span></div>
      <div class="row sub"><span>Add grilled or blackened tuna, salmon or shrimp...</span><span class="price">10.09</span></div></div>
    <div><div class="item-name">Heavenly Salad</div>
      <div class="row item-desc"><span>Romaine lettuce, bacon bits, grilled chicken, mandarin oranges, toasted almonds with poppy seed dressing.</span><span class="price">11.05</span></div></div>
    <div><div class="item-name">Super Spinach Salad</div>
      <div class="row item-desc"><span>Baby spinach, eggs, purple onions, bacon bits, roasted red peppers and bleu cheese crumbles.</span><span class="price">11.05</span></div>
      <div class="row sub"><span>With grilled or blackened chicken...</span><span class="price">13.05</span></div>
      <div class="row sub"><span>With grilled or blackened tuna, salmon or shrimp...</span><span class="price">15.05</span></div></div>
    <div><div class="item-name">Turkey Bowl</div>
      <div class="row item-desc"><span>A Caesar salad topped with pasta salad, cubed turkey breast and fresh grated parmesan.</span><span class="price">11.05</span></div></div>
    <div><div class="item-name">Chef Salad</div>
      <div class="row item-desc"><span>Lettuce, tomato, turkey, ham, shredded cheese, sliced eggs.</span><span class="price">11.05</span></div></div>
    <div><div class="item-name">Arugula Salad</div>
      <div class="row item-desc"><span>Arugula, candied walnuts, thinly sliced green apples, dried cranberries, bleu cheese, lemon herb vinaigrette</span><span class="price">11.25</span></div>
      <div class="row sub"><span>With grilled or blackened chicken breast</span><span class="price">13.25</span></div>
      <div class="row sub"><span>With blackened salmon, tuna, or shrimp</span><span class="price">15.05</span></div></div>
  </section>

  <!-- Drinks -->
  <div class="panel" style="left:40px;top:975px;width:374px;height:150px"></div>
  <section class="panel-body" style="left:58px;top:984px;width:338px;height:134px;justify-content:flex-start">
    <h2 style="text-align:center;font-size:26px;line-height:1.2">Drinks</h2>
    <div class="drinks-list">
      <div>Cola, Diet Cola, Cherry Cola, Lemon-Lime, Root Beer, Pepper Soda, Cream Soda, Tea, Raspberry Tea, Lemonade,</div>
      <div class="row"><span>Coffee (regular or decaf), Sparkling Mineral Water</span><span>2.49</span></div>
      <div class="row"><span>Bottled Water</span><span>1.95</span></div>
      <div class="row"><span>Premium Water</span><span>3.45</span></div>
      <div class="row"><span>Large Drinks</span><span>3.39</span></div>
    </div>
  </section>

  <!-- Brand name -->
  <div class="brand">
    <div class="brand-name">Tolbert’s</div>
  </div>

  <!-- Burgers & Dogs -->
  <div class="panel" style="left:430px;top:316px;width:297px;height:628px"></div>
  <div class="panel-cap" style="left:481px;top:259px;width:198px;height:72px"></div>
  <h2 class="panel-title" style="left:430px;width:297px;top:286px;font-size:23px">Burgers<br>&amp; Dogs</h2>
  <section class="panel-body burgers" style="left:446px;top:346px;width:268px;height:590px">
    <div class="item-desc" style="text-align:center;font-size:11.5px">Try it on a jalapeño bun! +1.20<br>add fried egg +1 add cheese +1</div>
    <div><div class="item-name">Tolbert’s Best Burger</div>
      <div class="row item-desc"><span>100% ground beef on a toasted bun.</span><span class="price">7.09</span></div></div>
    <div><div class="item-name">Tolbert Melt</div>
      <div class="row item-desc"><span>100% ground beef with Swiss cheese, served on rye bread.</span><span class="price">8.65</span></div></div>
    <div><div class="item-name">Super Burger</div>
      <div class="row item-desc"><span>Our “Best Burger” enhanced with bacon, avocado, Swiss and cheddar cheese, sprouts, served on a toasted bun.</span><span class="price">10.39</span></div></div>
    <div><div class="item-name">Jalapeño Burger</div>
      <div class="row item-desc"><span>100% ground beef with pepper jack cheese, bacon and served on a jalapeño bun.</span><span class="price">10.45</span></div></div>
    <div><div class="item-name">Green Chile Pepper Burger</div>
      <div class="row item-desc"><span>100% ground beef with green chile peppers, Swiss cheese on a toasted bun.</span><span class="price">9.95</span></div></div>
    <div><div class="item-name">Bacon Jam Arugula Burger</div>
      <div class="row item-desc"><span>100% ground beef with bacon jam, white cheddar, arugula and a drizzle of balsamic reduction on a toasted bun</span><span class="price">10.99</span></div></div>
    <div><div class="item-name">Hot Dog</div>
      <div class="row item-desc"><span>All beef frank.</span><span class="price">6.25</span></div></div>
    <div><div class="item-name">Chicago Dog</div>
      <div class="row item-desc"><span>All beef frank with hot giardiniera relish.</span><span class="price">6.50</span></div></div>
    <div><div class="item-name">Chili Dog</div>
      <div class="row item-desc"><span>All beef frank with chili, cheese, and onions.</span><span class="price">6.99</span></div></div>
    <div><div class="item-name">The Works Dog</div>
      <div class="row item-desc"><span>All beef frank with chili, cheese, and onions and giardiniera relish.</span><span class="price">7.25</span></div></div>
    <div><div class="item-name">Mac &amp; Cheese Dog</div>
      <div class="row item-desc"><span>All beef frank with mac &amp; cheese and green onion.</span><span class="price">7.75</span></div></div>
  </section>

  <!-- Quality note -->
  <div class="panel" style="left:430px;top:949px;width:297px;height:176px"></div>
  <section class="panel-body" style="left:446px;top:960px;width:265px;height:156px;justify-content:center">
    <p class="note">Only the finest ingredients, the choicest cuts of meats and the freshest produce will be good enough for our customers. Our beef products are from the round cut (leanest possible) therefore the most “heart healthy”. Our turkey is smoked breast 98% fat free. We make our salads fresh from scratch. We want you to know these facts so you will understand why we feel we are unique in the Crestvale Basin. To state our philosophy in a single word, it is <b>“QUALITY”</b></p>
  </section>

  <!-- Hot Sandwiches -->
  <div class="panel" style="left:745px;top:104px;width:374px;height:866px"></div>
  <div class="panel-cap" style="left:787px;top:36px;width:290px;height:82px"></div>
  <h2 class="panel-title" style="left:745px;width:374px;top:70px;font-size:28px">Hot<br>Sandwiches</h2>
  <section class="panel-body sandwiches" style="left:766px;top:150px;width:334px;height:808px">
    <div><div class="item-name">Grilled Cheese Sandwich</div>
      <div class="row item-desc"><span>Grilled with your choice of: Swiss, provolone, American, cheddar or pepper jack.</span><span class="price">6.25</span></div></div>
    <div><div class="item-name">Beer Brats</div>
      <div class="row item-desc"><span>Soaked in beer with grilled onions and sauerkraut on a toasted French roll.</span><span class="price">6.50</span></div></div>
    <div><div class="item-name">Beefeater</div>
      <div class="row item-desc"><span>Thin sliced roast beef on white bread with horseradish sauce, melted Swiss and tomato slices.</span><span class="price">9.35</span></div></div>
    <div><div class="item-name">French Dip</div>
      <div class="row item-desc"><span>Lean roast beef served on a steak bun with melted provolone, au jus c’est magnifique! Try it with <b>Chicago-Style Giardiniera</b> +1</span><span class="price">9.05</span></div></div>
    <div><div class="item-name">Philly</div>
      <div class="row item-desc"><span>Lean roast beef with grilled onions and cheddar cheese on a fresh baked French roll.</span><span class="price">10.35</span></div></div>
    <div><div class="item-name">Reuben</div>
      <div class="row item-desc"><span>Lean corned beef on grilled rye with melted Swiss, Reuben dressing and sauerkraut mmm good!</span><span class="price">10.05</span></div></div>
    <div><div class="item-name">Rachel (Turkey Reuben)</div>
      <div class="row item-desc"><span>Turkey on grilled rye with melted Swiss, Reuben dressing and sauerkraut.</span><span class="price">10.05</span></div></div>
    <div><div class="item-name">Hot Pastrami</div>
      <div class="row item-desc"><span>Served with Swiss on rye.</span><span class="price">9.35</span></div></div>
    <div><div class="item-name">Krabmelt</div>
      <div class="row item-desc"><span>Fresh krab salad, melted Swiss served on grilled rye bread.</span><span class="price">10.35</span></div></div>
    <div><div class="item-name">Grilled Chicken Sandwich</div>
      <div class="row item-desc"><span>Strips of grilled chicken breast served on a toasted bun with lettuce and tomato.</span><span class="price">9.75</span></div></div>
    <div><div class="item-name">Blackened Chicken Sandwich</div>
      <div class="row item-desc"><span>Strips of blackened chicken breast served on a whole wheat bun with lettuce and tomato</span><span class="price">9.75</span></div></div>
    <div><div class="item-name">Chik-ado</div>
      <div class="row item-desc"><span>Strips of marinated chicken on a wheat bun topped with bacon, pepper jack cheese, sprouts and avocado.</span><span class="price">10.15</span></div></div>
    <div><div class="item-name">Chicken Fried Steak Sandwich</div>
      <div class="row item-desc"><span>With lettuce and tomato on a toasted bun</span><span class="price">10.05</span></div></div>
    <div><div class="item-name">Veggie Pita</div>
      <div class="row item-desc"><span>Fresh garden veggies sautéed with olive oil, seasoned &amp; served in a pita pocket.</span><span class="price">9.05</span></div>
      <div class="row item-desc"><span>With grilled or blackened chicken breast</span><span class="price">11.09</span></div>
      <div class="row item-desc"><span>With grilled our blackened shrimp</span><span class="price">14.09</span></div>
      <div class="item-desc">Add 4 oz. hummus <b>+2.25</b> OR 4 oz. tzatziki <b>+1.25</b></div></div>
  </section>

  <!-- Contact -->
  <div class="panel" style="left:745px;top:975px;width:374px;height:150px"></div>
  <section class="panel-body contact" style="left:751px;top:981px;width:362px;height:138px;justify-content:center">
    <div>4820 W. Brannon</div>
    <div>Crestvale, Texas 79000</div>
    <div>(555)014-2290</div>
    <div>@tolberts_deli</div>
    <div>www.tolbertsonbrannon.com</div>
  </section>
</main>
</body>
</html>
```